Design a DL flyer double sided 4 colour 210mm x 95 mm (portrait) for the launch of a new yoga studio opening in North Melbourne on the 23 November 2013.
The final design should communicate with a strong call to action- the opening date , register to receive your first class free and like us on plain square.
The studio provides a tranquil, open space to practice yoga, create a feeling of light, peace and a nurturing environment, please create this feeling in the design.

An example design mock (rough design feel free to move around as required, includes final content) print specifications, logo, typography style and image attached.
The reverse side to include logo, address and please design the timetable for the launch week (refer design mock)
Have also attached a reverse logo for a dark background and are open to designer providing examples with various background colours and effects.
Back content can be moved to the front side if required to facilitate design

Target Market(s)

People in the area who are practicing yoga elsewhere and encourage them to come to the studio to try us out with a free opening offer in our first week. And people new to yoga wanting to give it a try.
Experienced yoga people and people new to yoga - all ages

Industry/Entity Type

Environment

Requirements
Must have
• The Calm Haven logo physical address, website address, the tagline rest, stretch, renew
The final design should communicate with a strong call to action- the opening date , register to receive your first class free and like us on plain square. and the website address thecalmhaven.com.au, drive them to the website to register.
The studio provides a tranquil, open space to practice yoga, create a feeling of light, peace and a nurturing environment, please create this feeling in the design

```html
<!DOCTYPE html>
<html lang="en">
<head>
<meta charset="utf-8">
<title>The Calm Haven – Opening Flyer</title>
<link href="https://fonts.googleapis.com/css2?family=Mulish:ital,wght@0,400;0,700;0,800;1,800;1,900&family=Ubuntu:ital,wght@0,400;0,500;0,700;1,400&display=swap" rel="stylesheet">
<style>
  :root{
    --green:#3f8f3a;
    --green-deep:#2f7a2c;
    --orange:#e8821f;
    --orange-deep:#d9661a;
    --cream:#eeeed6;
    --cream-light:#f4f4e4;
    --ink:#1e1e1e;
    --charcoal:#4a4a4a;
    --grey-band:#565656;
    --chip:#4b4b4b;
    --text-grey:#555555;
    --stage:#ffffff;
  }
  *{box-sizing:border-box;margin:0;padding:0}
  html,body{width:963px;height:1200px;overflow:hidden;background:var(--stage)}
  .stage{position:relative;width:963px;height:1200px}
  .flyer{position:absolute;top:136px;width:420px;height:928px;overflow:hidden;box-shadow:0 4px 18px rgba(0,0,0,.25)}
  .flyer--front{left:40px;background:var(--cream)}
  .flyer--back{left:503px;background:linear-gradient(180deg,var(--cream-light),var(--cream))}

  /* studio name block */
  .brand{position:absolute;left:0;right:0;text-align:center;font-family:'Ubuntu',sans-serif}
  .brand__name{display:inline-flex;align-items:center;gap:10px;font-size:32px;font-weight:700;color:var(--orange)}
  .brand__dot{width:16px;height:16px;border-radius:50%;background:var(--orange)}
  .brand__motto{font-size:15px;font-weight:400;letter-spacing:2px;text-transform:uppercase;margin-top:4px}

  /* front */
  .hero-photo{position:absolute;inset:0 0 auto 0;height:650px;
    background:radial-gradient(ellipse at 55% 55%,#c9c8bf 0%,#8fa58a 22%,#4d7a3a 50%,#2d5a24 80%,#1f4519 100%)}
  .front-brand{top:44px}
  .front-brand .brand__name{color:#fff}
  .front-brand .brand__motto{color:#f3e2c8}
  .studio-banner{position:absolute;top:148px;left:0;width:100%;height:62px;background:rgba(235,235,215,.72);
    font-family:'Mulish',sans-serif;font-style:italic;font-weight:900;font-size:37px;color:#1f2a1a;
    display:flex;align-items:center;justify-content:center}
  .opening-tag{position:absolute;top:214px;left:0;height:40px;padding:0 18px 0 40px;background:var(--green);
    font-family:'Mulish',sans-serif;font-style:italic;font-weight:800;font-size:24px;color:#fff;display:flex;align-items:center}
  .offer-band{position:absolute;top:640px;left:0;width:100%;height:62px;background:var(--orange);
    display:flex;align-items:center;justify-content:center;gap:10px;
    font-family:'Mulish',sans-serif;font-style:italic;font-weight:900;font-size:38px;color:#fff}
  .offer-band__lead{background:var(--green);padding:2px 10px}
  .dates-band{position:absolute;top:702px;left:90px;right:0;height:40px;background:var(--ink);
    font-family:'Mulish',sans-serif;font-style:italic;font-weight:800;font-size:22px;color:#fff;
    display:flex;align-items:center;justify-content:center}
  .booking{position:absolute;top:752px;left:0;right:0;text-align:center;font-family:'Mulish',sans-serif}
  .booking__title{font-size:29px;font-weight:800;color:var(--ink);line-height:1.1}
  .booking__sub{font-size:18px;font-weight:700;color:var(--green);line-height:1.2}
  .booking__url{font-size:25px;font-weight:800;font-style:italic;color:var(--green-deep);margin-top:12px}
  .address-footer{position:absolute;bottom:0;left:0;width:100%;height:68px;background:var(--green);
    font-family:'Mulish',sans-serif;font-weight:800;font-size:16px;color:#fff;letter-spacing:.3px;
    display:flex;align-items:center;justify-content:center}

  /* back */
  .intro{position:absolute;top:44px;left:40px;right:40px;text-align:center;font-family:'Ubuntu',sans-serif;font-size:12.5px;line-height:1.32;color:var(--text-grey)}
  .intro p{margin-bottom:11px}
  .intro .intro__accent{color:var(--green);font-style:italic}
  .timetable__heading{position:absolute;top:268px;left:110px;right:0;height:34px;background:var(--grey-band);
    font-family:'Ubuntu',sans-serif;font-style:italic;font-weight:500;font-size:19px;color:#fff;display:flex;align-items:center;padding-left:14px}
  .timetable{position:absolute;top:312px;left:108px;font-family:'Ubuntu',sans-serif}
  .timetable__day{font-weight:700;font-size:19px;color:var(--orange);margin-bottom:4px;letter-spacing:-.3px}
  .timetable__slots{display:flex;flex-wrap:wrap;gap:5px 6px;width:160px;margin-bottom:12px}
  .slot{background:var(--chip);color:#fff;font-size:9.5px;font-weight:500;padding:4px 5px;border:1px solid #9a9a9a}
  .social{position:absolute;top:520px;left:75px;display:flex;align-items:center;gap:7px;font-family:'Ubuntu',sans-serif;font-size:17px;color:var(--charcoal)}
  .social__square{width:20px;height:20px;background:#3b5ea0}
  .specials{position:absolute;top:556px;left:0;right:0;text-align:center;font-family:'Mulish',sans-serif}
  .specials__title{font-size:19px;font-weight:800;color:var(--ink)}
  .specials__url{font-size:13px;font-weight:800;color:var(--green-deep)}
  .map-band{position:absolute;top:665px;left:0;width:100%;height:56px;background:var(--grey-band)}
  .map{position:absolute;top:620px;left:140px;width:225px;height:140px;border:4px solid var(--orange);border-radius:18px;
    background:linear-gradient(135deg,#e9e6dc,#d8d4c4 55%,#e8d9a0)}
  .back-brand{top:810px}
  .back-brand .brand__name{font-size:34px}
  .back-brand .brand__motto{color:var(--charcoal)}
  .back-address{position:absolute;top:886px;left:0;right:0;text-align:center;font-family:'Mulish',sans-serif;font-weight:800;font-size:15px;color:var(--orange-deep)}
</style>
</head>
<body>
<main class="stage">

  <section class="flyer flyer--front" aria-label="Flyer front">
    <div class="hero-photo" role="img" aria-label="Photo: woman in white meditating cross-legged beside still water in a green rainforest"></div>
    <div class="brand front-brand">
      <div class="brand__name"><span class="brand__dot"></span>The Calm Haven</div>
      <div class="brand__motto">rest, stretch, renew</div>
    </div>
    <div class="studio-banner">New Yoga Studio</div>
    <div class="opening-tag">Opening 23 Nov</div>
    <div class="offer-band"><span class="offer-band__lead">First Class</span><span>FREE</span></div>
    <div class="dates-band">23 Nov – 29 Nov inclusive</div>
    <div class="booking">
      <div class="booking__title">To book your free class</div>
      <div class="booking__sub">go online to register and book</div>
      <div class="booking__url">www.thecalmhaven.com.au</div>
    </div>
    <div class="address-footer">48 WATTLE LANE, NORTH MELBOURNE</div>
  </section>

  <section class="flyer flyer--back" aria-label="Flyer back">
    <div class="intro">
      <p>A generously sized natural studio in North Melbourne, providing dynamic flow vinyasa and restorative yoga for all levels from newbies to experienced, with a collection of the best teachers.</p>
      <p class="intro__accent">Embark on a journey to happiness within yourself – be healthy in your body and mind.</p>
      <p>Science is finally proving what yogis have known all along.... <span class="intro__accent">yoga is good for you!</span></p>
      <p>A tranquil space to de stress, build strength and healing in our bodies through our own tapas (internal heat).</p>
    </div>

    <div class="timetable__heading">Class Times</div>
    <div class="timetable">
      <div class="timetable__day">Sat</div>
      <div class="timetable__slots"><span class="slot">9.00 AM</span><span class="slot">10.30 AM</span><span class="slot">4.00 PM</span></div>
      <div class="timetable__day">Sun</div>
      <div class="timetable__slots"><span class="slot">9.00 AM</span><span class="slot">10.30 AM</span><span class="slot">4.00 PM</span></div>
      <div class="timetable__day">Mon - Fri</div>
      <div class="timetable__slots"><span class="slot">6.30 AM</span><span class="slot">9.30 AM</span><span class="slot">12.30 PM</span><span class="slot">5.30 PM</span><span class="slot">7.00 PM</span></div>
    </div>

    <div class="social"><span class="social__square"></span>The Calm Haven - Melbourne</div>
    <div class="specials">
      <div class="specials__title">View other opening specials</div>
      <div class="specials__url">www.thecalmhaven.com.au</div>
    </div>

    <div class="map-band"></div>
    <div class="map" role="img" aria-label="Street map of North Melbourne showing the studio location"></div>

    <div class="brand back-brand">
      <div class="brand__name"><span class="brand__dot"></span>The Calm Haven</div>
      <div class="brand__motto">rest, stretch, renew</div>
    </div>
    <div class="back-address">48 WATTLE LANE, NORTH MELBOURNE</div>
  </section>

</main>
</body>
</html>
```